Business Card Design for Marketing Firm

Looking for business card design for higher end marketing firm. Clean but impressionable/trendy. We are a marketing firm that represents manufacturers in the foodservice equipment and supply industry. Our customers are end users such has hotels, restaurants, country clubs, convention centers and casinos as well as distributors of restaurants supplies and equipment, and manufacturers of foodservice equipment and supplies.
Target Market(s)
Hotels, Restaurants, Supply & Equipment Distributors, Foodservice Manufacturers
Industry/Entity Type
Foodservice/Hospitality
Contact Information for Business Card
Name, Title, Contact Number, Email, Website, Social Media, Address
Requirements
Must have
- Clean & Simple but Serious and Impressionable

```html
<!DOCTYPE html>
<html lang="en">
<head>
<meta charset="utf-8">
<title>Meridian Reps – Business Card</title>
<link rel="stylesheet" href="https://fonts.googleapis.com/css2?family=EB+Garamond:wght@400;600;700&display=swap">
<style>
  :root {
    --backdrop: #8e8e8e;
    --navy: #000080;
    --paper: #ffffff;
    --ink: #4a4a4a;
    --rule: #555555;
  }
  * { margin: 0; padding: 0; box-sizing: border-box; }
  html, body { width: 1200px; height: 1200px; overflow: hidden; }
  body {
    background: var(--backdrop);
    font-family: "EB Garamond", Georgia, serif;
    position: relative;
  }
  .card {
    position: absolute;
    left: 250px;
    width: 700px;
    height: 400px;
    border-radius: 20px;
    box-shadow: 0 3px 8px rgba(0,0,0,0.25);
  }
  .card--front { top: 170px; background: var(--paper); }
  .card--back { top: 631px; background: var(--navy); }

  .brand {
    position: absolute;
    display: flex;
    flex-direction: column;
    align-items: center;
  }
  .brand__dot { border-radius: 50%; }
  .brand__name {
    font-weight: 600;
    letter-spacing: 0.04em;
    white-space: nowrap;
    line-height: 1;
  }
  .card--front .brand { left: 67px; width: 267px; top: 115px; }
  .card--front .brand__dot { width: 54px; height: 54px; background: var(--navy); margin-bottom: 22px; }
  .card--front .brand__name { font-size: 31px; color: var(--navy); }

  .card--back .brand { left: 0; width: 700px; top: 105px; }
  .card--back .brand__dot { width: 100px; height: 100px; background: var(--paper); margin-bottom: 34px; }
  .card--back .brand__name { font-size: 56px; color: var(--paper); }

  .divider {
    position: absolute;
    left: 367px;
    top: 100px;
    width: 1px;
    height: 200px;
    background: var(--rule);
  }
  .person { position: absolute; left: 401px; top: 93px; }
  .person__name {
    font-size: 32px;
    font-weight: 700;
    color: var(--navy);
    letter-spacing: 0.05em;
    line-height: 1;
  }
  .person__title { font-size: 19px; color: var(--ink); margin-top: 4px; letter-spacing: 0.02em; }

  .contact { position: absolute; left: 401px; list-style: none; color: var(--ink); }
  .contact__item { display: flex; align-items: flex-start; }
  .contact__icon { width: 16px; height: 16px; flex: none; margin-right: 11px; margin-top: 3px; fill: var(--navy); }
  .contact__text { font-size: 16px; line-height: 24px; }
  .contact--address { top: 171px; }
  .contact--lines { top: 228px; }
  .contact--lines .contact__item { height: 25px; }
  .contact__text--phone { font-size: 19px; }
</style>
</head>
<body>
  <section class="card card--front">
    <div class="brand">
      <span class="brand__dot"></span>
      <span class="brand__name">MERIDIAN REPS</span>
    </div>
    <div class="divider"></div>
    <div class="person">
      <p class="person__name">DALE MORGAN</p>
      <p class="person__title">Founder &amp; CEO</p>
    </div>
    <ul class="contact contact--address">
      <li class="contact__item">
        <svg class="contact__icon" viewBox="0 0 16 16"><path d="M8 0a5.5 5.5 0 0 0-5.5 5.5C2.5 9.6 8 16 8 16s5.5-6.4 5.5-10.5A5.5 5.5 0 0 0 8 0zm0 7.8a2.3 2.3 0 1 1 0-4.6 2.3 2.3 0 0 1 0 4.6z"/></svg>
        <span class="contact__text">4780 Alder Court<br>Milford, CT 06460</span>
      </li>
    </ul>
    <ul class="contact contact--lines">
      <li class="contact__item">
        <svg class="contact__icon" viewBox="0 0 16 16"><path d="M3.6 1l2.3 3-1.4 1.6c.9 2 2.5 3.6 4.5 4.5l1.6-1.4 3 2.3-1.3 2.6C7 13.6 2.4 9 1 3.6z"/></svg>
        <span class="contact__text contact__text--phone">(203) 555-0147</span>
      </li>
      <li class="contact__item">
        <svg class="contact__icon" viewBox="0 0 16 16"><path d="M1 3h14v10H1zm1.5 1.3V12h11V4.3L8 8.5z M2.8 4 8 7.8 13.2 4z"/></svg>
        <span class="contact__text">info@meridianreps.com</span>
      </li>
      <li class="contact__item">
        <svg class="contact__icon" viewBox="0 0 16 16"><circle cx="8" cy="8" r="6.5" fill="none" stroke="#000080" stroke-width="1.6"/><path d="M5 4.5l2 1.5-.5 2 1.5 1.5-.5 3-2-2.5-1.5-3zM10 4l2 2-1 2-1.5-1z"/></svg>
        <span class="contact__text">meridianreps.com</span>
      </li>
    </ul>
  </section>

  <section class="card card--back">
    <div class="brand">
      <span class="brand__dot"></span>
      <span class="brand__name">MERIDIAN REPS</span>
    </div>
  </section>
</body>
</html>
```